Lanterns on the Tide

I need a book cover design for a world history book written for a target audience of high school students and progressive teachers. The book is more balanced towards a world history perspective than a Western-leaning perspective. The first 500 pages deal with the major turning points in world history - from the first hominids that roamed Africa to the end of the Cold War, and the final 100 pages cover the major challenges facing the world today. The book is 95% graphic details, hopefully-engaging stories and needed facts, but there is a bit of sarcasm, verbal irony and asides thrown in to keep the reader's eyes from glossing over. I would need a cover that would appeal to any school teacher, but something that would not scare off students or the average Joe off the street.
Updates

One added note, please leave the bottom right corner -  2" height by 3" width free of text/image for the ISBN code.

As far as a central image goes, it needs to be a dynamic (avoid something readers would readily see elsewhere in their lives) image, or nothing at all.  Also, please justify all text on the back cover to the left side (avoid centering).

Reason: A few people have voiced an interest in having the deadline extended through next weekend to allow for some alterations and also the ability to take advantage of the upcoming holidays. I will take you up on this request. Thank you all again for your submissions. i've seen some very unique takes on the story/tone of the book.

Industry/Entity Type

High School

Requirements
Must have
• I've enclosed a PDF with the text for the front and back cover.

On the back cover, I'd like the quote and the initial question to stand out. I'd like the initial question to be in lower case.

For the spine, I'd like the title font to match the title front from the front cover.

The book cover needs to measure 9.25" by 13.75" with a 1.5" spine. Allow .125 inches for the bleed.

I've attached a Word Document with all the text. The layout is just a suggestion.
Should not have
• I do not want any stock images that I'll need to pay for.

```html
<!DOCTYPE html>
<html lang="en">
<head>
<meta charset="utf-8">
<title>Lanterns on the Tide – Book Cover</title>
<link rel="stylesheet" href="https://fonts.googleapis.com/css2?family=Open+Sans:ital,wght@0,400;0,700;1,700&family=Questrial&family=Mulish:wght@700;800&display=swap">
<style>
  :root {
    --sky: #35c4ef;
    --coral: #f58b58;
    --grass: #46b64a;
    --isbn: #b2a58b;
    --paper: #ffffff;
  }
  html, body {
    margin: 0;
    padding: 0;
    width: 1200px;
    height: 807px;
    overflow: hidden;
    background: var(--grass);
  }
  .cover {
    position: relative;
    width: 1200px;
    height: 807px;
    background: var(--grass);
    color: var(--paper);
    overflow: hidden;
  }
  .band-sky {
    position: absolute;
    left: 0; top: 0;
    width: 1200px; height: 121px;
    background: var(--sky);
  }
  .band-coral {
    position: absolute;
    left: 0; top: 121px;
    width: 1200px; height: 43px;
    background: var(--coral);
  }
  .back-question {
    position: absolute;
    left: 34px; top: 17px;
    width: 480px;
    margin: 0;
    font-family: "Open Sans", Arial, sans-serif;
    font-weight: 700;
    font-size: 28px;
    line-height: 39px;
  }
  .back-blurb {
    position: absolute;
    left: 79px; top: 181px;
    width: 412px;
    font-family: "Questrial", "Century Gothic", sans-serif;
    font-size: 12px;
    line-height: 16px;
    text-align: left;
  }
  .back-blurb p {
    margin: 0 0 15px;
  }
  .back-quote {
    position: absolute;
    left: 79px; top: 527px;
    width: 412px;
    margin: 0;
    font-family: "Open Sans", Arial, sans-serif;
    font-style: italic;
    font-weight: 700;
    font-size: 12px;
    line-height: 21.5px;
  }
  .back-quote .mark {
    font-size: 20px;
    line-height: 0;
  }
  .isbn-space {
    position: absolute;
    left: 273px; top: 632px;
    width: 260px; height: 175px;
    background: var(--isbn);
  }
  .spine-title {
    position: absolute;
    left: 606px; top: 212px;
    transform-origin: 0 0;
    transform: rotate(90deg) translateY(-50%);
    white-space: nowrap;
    font-family: "Mulish", "Century Gothic", sans-serif;
    font-weight: 700;
    font-size: 36px;
    letter-spacing: 0.5px;
  }
  .spine-author {
    position: absolute;
    left: 544px; top: 690px;
    width: 112px;
    margin: 0;
    font-family: "Open Sans", Arial, sans-serif;
    font-weight: 700;
    font-size: 21px;
    line-height: 29px;
    letter-spacing: 1.5px;
    text-align: center;
  }
  .front-author {
    position: absolute;
    left: 727px; top: 60px;
    width: 412px;
    margin: 0;
    font-family: "Open Sans", Arial, sans-serif;
    font-weight: 700;
    font-size: 32px;
    letter-spacing: 4px;
    text-align: center;
  }
  .front-title {
    position: absolute;
    left: 727px; top: 300px;
    width: 440px;
    margin: 0;
    font-family: "Mulish", "Century Gothic", sans-serif;
    font-weight: 800;
    text-align: center;
    line-height: 1;
  }
  .front-title .title-lead {
    display: block;
    font-size: 74px;
    letter-spacing: 1px;
    transform: scaleY(1.45);
    transform-origin: 50% 100%;
  }
  .front-title .title-tail {
    display: block;
    margin-top: 14px;
    font-size: 62px;
    transform: rotate(-3deg) scaleY(1.2);
  }
  .front-subtitle {
    position: absolute;
    left: 755px; top: 650px;
    width: 440px;
    margin: 0;
    font-family: "Questrial", "Century Gothic", sans-serif;
    font-size: 23px;
    line-height: 28px;
  }
</style>
</head>
<body>
<main class="cover">
  <div class="band-sky"></div>
  <div class="band-coral"></div>

  <section class="back-cover">
    <h2 class="back-question">Do you have any idea &nbsp;how we got to here?</h2>

    <div class="back-blurb">
      <p>Well, if you're like 97.4% of the people walking the planet, you haven't got a clue. &nbsp;Sure, you might know a bit about a couple rivers in Mesopotamia, how Philon Kastor wandered around Athens asking questions or how Matthias Lenhart got ticked off one day and nailed a really long essay to the door of a church. &nbsp;But to be honest (and don't be embarrassed), you've got some gaps.</p>
      <p>Be dense no more. &nbsp;In Lanterns on the Tide, Daniel Hartwell takes you through all the major tales, traditions and turning points of world history – not just European history, but WORLD history. &nbsp;You'll figure out real quick that the West might have had some crowning moments, but for the whole of human history, it's been the Persians, the Indians, the Chinese, the Muslims or some horse peoples from the steppe that have truly turned us into the clever little creatures we are today.</p>
      <p>And when most world history books fade off once the Cold War comes to a close, this sometimes cheekily-written tome just gets going. &nbsp;It finished with a distinctively comprehensive look at the 21st century challenges facing the nine major regions of today's world – Africa, Latin America, Japan, China, the Middle East, India, Russia, Europe and the United States.</p>
    </div>

    <blockquote class="back-quote"><span class="mark">“</span>Daniel Hartwell expertly understands exactly what his audience wants to know, what they need to know. &nbsp;A page-turning account of our proudest achievements and our most colossal bumblings. It's world history for the rest of us.<span class="mark">”</span> – Amara Qusaybi</blockquote>

    <div class="isbn-space"></div>
  </section>

  <section class="spine">
    <div class="spine-title">LANTERNS on the Tide</div>
    <p class="spine-author">DANIEL<br>HARTWELL</p>
  </section>

  <section class="front-cover">
    <p class="front-author">DANIEL HARTWELL</p>
    <h1 class="front-title">
      <span class="title-lead">LANTERNS</span>
      <span class="title-tail">on the Tide</span>
    </h1>
    <p class="front-subtitle">The tales, traditions and<br>turning points of world history<br>and the regional challenges of today</p>
  </section>
</main>
</body>
</html>
```